Business card for Les Brisants-Marins campsite

HORIZONTAL / 85x55
OBJECTIVE
Create a modern, attractive and memorable business card for the Les Brisants-Marins campsite, located on the Île d'Oléron.
The map should make people want to discover the campsite and immediately convey its world: ocean, holidays, nature and conviviality.
VISUAL IDENTITY
The design must be in the same graphic style as our website:
www.lesbrisants-marins.fr
The site is the main reference for the visual atmosphere: colours, typography, shapes, photographs and general universe.
The map and the site must give the impression of belonging to a single brand identity.
A UNIVERSE TO TRANSMIT
• Île d'Oléron
• Atlantic Ocean
• Seaside
• Direct access to the beaches
• Vacation
• Nature
• Family-friendly and welcoming atmosphere
• Relaxation
DESIRED STYLE
Bright, warm, modern, nautical and natural.
We want a creation with a real personality, immediately recognizable, and not a generic camping business card.
FRONT
Prioritize visual impact with:
• Official logo Les Brisants-Marins
• Île d'Oléron
• A strong evocation of the ocean and holidays
• A short and memorable hook
The designer is free to propose their own hook.
BACK
The Marine Breakers
Villages 1 & 2
22 Rue des Vergnes
17310 Saint-Pierre-d'Oléron
France
Tel.: +33 5 46 82 13 47
www.lesbrisants-marins. fr
Possibility of discreet integration:
Direct access to the beaches
Mobile homes • Pitches • Accommodation
Le Varech Bar-Restaurant
FORMAT
Double-sided card: 85 × 55 mm.
Horizontal orientation
AVOID
• Overly institutional design
• Overloaded map
• Generic "camping" style
• Too many pictograms
• Accumulation of texts
• Modification or distortion of the official logo
• Graphic design unrelated to the website
CREATIVE FREEDOM
We are looking for an original proposal.
The designer can play with the graphic codes of the ocean, waves, sun, beach and Île d'Oléron, while remaining faithful to the visual identity of the site.
The card must be aesthetically pleasing and original enough to make people want to keep it.
The objective:
See the map → think about the ocean and holidays → remember Les Brisants-Marins → discover the campsite.
Target Market(s)
All targets
Industry/Entity Type
Tourisme
Contact Information for Business Card
adresse, téléphone, email, site internet + réseaux sociaux
Look and feel
Each slider illustrates characteristics of the customer's brand and the style your logo design should communicate.

```html
<!DOCTYPE html>
<html lang="en">
<head>
<meta charset="utf-8">
<title>Les Brisants-Marins – Business card</title>
<link rel="stylesheet" href="https://fonts.googleapis.com/css2?family=Lora:wght@600;700&family=Montserrat:wght@400;500;600&family=Allura&display=swap">
<style>
  :root{
    --navy:#17305a;
    --navy-deep:#132a4f;
    --green:#8cb82e;
    --paper:#f6f4ef;
    --bg:#dfe2e6;
    --sand:#e6d7b8;
    --sea:#94b6cf;
    --ink:#26384f;
    --rule:#9aa3ae;
    --white:#ffffff;
  }
  *{margin:0;padding:0;box-sizing:border-box}
  html,body{width:1200px;height:777px;overflow:hidden;background:var(--bg)}
  .sheet{position:relative;width:1200px;height:777px;display:flex;align-items:center;justify-content:center;gap:20px}
  .card{position:relative;width:570px;height:369px;background:var(--paper);overflow:hidden;box-shadow:0 4px 14px rgba(20,40,70,.18)}
  .card svg.layer{position:absolute;inset:0;width:100%;height:100%}

  /* front */
  .brand{position:absolute;left:118px;top:50px;width:330px}
  .brand-island{font-family:"Montserrat",sans-serif;font-weight:600;font-size:10.5px;letter-spacing:3px;color:var(--green);margin-left:74px}
  .brand-name{display:flex;align-items:center;gap:12px;margin-top:4px}
  .brand-dot{width:30px;height:30px;border-radius:50%;background:var(--green);flex:none}
  .brand-text{font-family:"Lora",serif;font-weight:700;font-size:40px;line-height:.98;color:var(--navy)}
  .brand-camping{font-family:"Montserrat",sans-serif;font-weight:600;font-size:11px;letter-spacing:3.4px;color:var(--green);margin:10px 0 0 96px}
  .hook{position:absolute;left:196px;top:212px;font-family:"Allura",cursive;line-height:.95;color:var(--navy)}
  .hook span{display:block}
  .hook .l1{font-size:38px}
  .hook .l2{font-size:38px;color:var(--green);margin-left:-8px}
  .hook .l3{font-size:34px;margin-left:80px}

  /* back */
  .services{position:absolute;left:36px;top:36px;width:184px}
  .services-head{display:flex;align-items:center;gap:8px;margin-bottom:16px}
  .services-dot{width:22px;height:22px;border-radius:50%;background:var(--green);flex:none}
  .services-title{font-family:"Allura",cursive;font-size:22px;line-height:.9;color:var(--navy)}
  .services-title em{font-style:normal;color:var(--green);display:block;margin-left:12px}
  .service{display:flex;align-items:center;gap:14px;border-top:1px solid var(--rule);height:44px;font-family:"Montserrat",sans-serif;font-weight:500;font-size:12.5px;color:var(--ink)}
  .service svg{width:30px;height:26px;flex:none;stroke:var(--ink);fill:none;stroke-width:1.4;stroke-linecap:round;stroke-linejoin:round}
  .service.two{line-height:1.15}

  .contact{position:absolute;left:316px;top:36px;width:240px;color:var(--white);font-family:"Montserrat",sans-serif}
  .contact-script{font-family:"Allura",cursive;font-size:26px;color:var(--green);line-height:1}
  .contact-villages{font-size:16px;font-weight:500;margin-top:2px}
  .contact-rule{width:120px;height:1px;background:var(--green);margin:14px 0 16px}
  .contact-row{display:flex;gap:14px;font-size:12.5px;line-height:1.6;margin-bottom:14px}
  .contact-row svg{width:20px;height:20px;flex:none;stroke:var(--green);fill:none;stroke-width:1.5;stroke-linecap:round;stroke-linejoin:round;margin-top:1px}
  .social{display:flex;gap:12px;margin-top:4px}
  .social span{width:26px;height:26px;border-radius:50%;border:1.5px solid var(--green)}
</style>
</head>
<body>
<main class="sheet">

  <section class="card card-front">
    <svg class="layer" viewBox="0 0 570 369" preserveAspectRatio="none">
      <defs>
        <linearGradient id="photo-tone" x1="0" y1="1" x2="1" y2="0">
          <stop offset="0" stop-color="var(--sand)"/>
          <stop offset="1" stop-color="var(--sea)"/>
        </linearGradient>
        <linearGradient id="paperfade" x1="0" y1="0" x2="0" y2="1">
          <stop offset="0" stop-color="var(--paper)"/>
          <stop offset=".6" stop-color="var(--paper)"/>
          <stop offset="1" stop-color="var(--paper)" stop-opacity="0"/>
        </linearGradient>
      </defs>
      <rect width="570" height="369" fill="url(#photo-tone)" role="img" aria-label="Photograph of an Atlantic beach at sunset with dune grass and a wooden fence along the path"/>
      <path d="M0 0H570V118C548 112 540 140 515 150C480 162 470 170 455 200C440 232 410 230 360 232C300 234 200 236 120 230C70 226 30 222 0 222Z" fill="url(#paperfade)"/>
    </svg>

    <div class="brand">
      <div class="brand-island">ÎLE D'OLÉRON</div>
      <div class="brand-name">
        <span class="brand-dot"></span>
        <div class="brand-text">Les Brisants<br>Marins</div>
      </div>
      <div class="brand-camping">CAMPING ★★★★</div>
    </div>

    <p class="hook">
      <span class="l1">Votre île,</span>
      <span class="l2">votre parenthèse</span>
      <span class="l3">océane</span>
    </p>
  </section>

  <section class="card card-back">
    <svg class="layer" viewBox="0 0 570 369" preserveAspectRatio="none">
      <defs>
        <linearGradient id="wave" x1="0" y1="0" x2="0" y2="1">
          <stop offset="0" stop-color="#a9c6dd"/>
          <stop offset="1" stop-color="#2d5a8a"/>
        </linearGradient>
      </defs>
      <path d="M0 310C80 300 160 318 240 340C255 344 265 356 270 369H0Z" fill="url(#wave)" role="img" aria-label="Photograph of ocean waves"/>
      <path d="M320 0H570V369H215C270 330 290 290 275 230C262 180 255 130 270 80C280 45 295 18 320 0Z" fill="#7ea6c8"/>
      <path d="M326 0H570V369H224C278 330 298 290 283 230C270 180 263 130 278 80C288 45 302 18 326 0Z" fill="var(--navy-deep)"/>
    </svg>

    <div class="services">
      <div class="services-head">
        <span class="services-dot"></span>
        <div class="services-title">Direct access<em>to the beaches</em></div>
      </div>
      <div class="service">
        <svg viewBox="0 0 30 26"><path d="M2 10L15 4L28 10V22H2Z"/><path d="M2 22H28M7 22V13H12V22M16 13H24V18H16Z"/></svg>
        Mobile homes
      </div>
      <div class="service">
        <svg viewBox="0 0 30 26"><path d="M3 23L12 5L21 23Z"/><path d="M12 5V23M9 23L12 16L15 23"/><path d="M24 11L20 18H28Z"/><path d="M24 18V23"/></svg>
        Pitches
      </div>
      <div class="service">
        <svg viewBox="0 0 30 26"><circle cx="21" cy="8" r="5"/><path d="M17 12L4 23M8 20L11 23M11 17L13 19"/></svg>
        Accommodation
      </div>
      <div class="service two">
        <svg viewBox="0 0 30 26"><path d="M8 3V23M5 3V9C5 11 11 11 11 9V3"/><path d="M20 23V3C17 6 17 13 20 14"/></svg>
        <span>Le Varech<br>Bar-Restaurant</span>
      </div>
    </div>

    <div class="contact">
      <div class="contact-script">The Marine Breakers</div>
      <div class="contact-villages">Villages 1 &amp; 2</div>
      <div class="contact-rule"></div>
      <div class="contact-row">
        <svg viewBox="0 0 20 20"><path d="M10 19C10 19 4 12 4 8A6 6 0 0 1 16 8C16 12 10 19 10 19Z"/><circle cx="10" cy="8" r="2.2"/></svg>
        <span>22 Rue des Vergnes<br>17310 Saint-Pierre-d'Oléron<br>France</span>
      </div>
      <div class="contact-row">
        <svg viewBox="0 0 20 20"><path d="M4 2L7 2L9 6L7 8C8 11 10 13 13 14L15 12L19 14V17C19 18 18 19 17 19C9 18 3 12 2 4C2 3 3 2 4 2Z"/></svg>
        <span>Tel.: +33 5 46 82 13 47</span>
      </div>
      <div class="contact-row">
        <svg viewBox="0 0 20 20"><circle cx="10" cy="10" r="8"/><path d="M2 10H18M10 2C6 6 6 14 10 18M10 2C14 6 14 14 10 18M4 5.5H16M4 14.5H16"/></svg>
        <span>www.lesbrisants-marins.fr</span>
      </div>
      <div class="social"><span></span><span></span><span></span></div>
    </div>
  </section>

</main>
</body>
</html>
```